Brickpress Design for a website design company

Web Design for a Web Design Company - As odd as that sounds, it is exactly right. We are a website design company with over 120 regular clients, we want to redesign our current website and take it to the next level. The problem we are finding is that we are too "inside the box". Which is why we are looking outside for a designer that will take us to the next level. We need this design to look STATE OF THE ART! Obviously there is allot we can do internally once we have a completed design to wrap up the project. So what we are looking for are some design concepts based on some ideas that we will provide. Once the concept is finalized we will need the layered design and any graphics that were used in separate files. If you have any questions please send them to us privately.

Example websites of how we want to look are:

1. http://www.brivlo.example
2. http://www.plumtavern.example
3. http://zelvaworks.example
4. http://www.kup.example
5. http://www.tarnleaf.example

Our current website we are redesigning is: www.frostlanewd.example

Navigation / Pages for new website are as follows:

Home
Services (page with broad detailing)
Portfolio
RFQ
Testimonials
About
Contact

Website Design
Website Re-design
Ecommerce
Mobile Websites
Copywriting
Hosting and Maintenance
Content Marketing
Pay Per Click Marketing
Mobile Text Marketing
Local Search Marketing

Design must be brickpress compatible, we use the meridian framework specifically.
Target Market(s)
Our target market is B2B, we want to sell web and marketing products
Requirements
Must Have:
- Design must be brickpress compatible, we use the meridian framework specifically.

As a bonus, if we like your work we may use you for our own clients...

Marcus

Industry/Entity Type

Marketing

Requirements
Must have
• For the content area - intro paragraph and blog categories below the header/banner area,

Need to include both shaded content "buttons" with graphics similar to the website attached jpg file titled - bottom content area

and hanging shaded ribbons from pixvault.example - attached jpg file titled: stock-illustration-57310268-glossy-promoting-badges

```html
<!DOCTYPE html>
<html lang="en">
<head>
<meta charset="utf-8">
<title>FrostLane Website Design</title>
<link href="https://fonts.googleapis.com/css2?family=Rosario:wght@400;600&family=Noto+Serif&display=swap" rel="stylesheet">
<style>
:root{
  --blue:#1a9ad6;
  --navy:#0d3d5e;
  --orange:#f39a1a;
  --orange-light:#fbc35a;
  --text:#444;
  --page:#f6f6f6;
  --dots:#9fc7e2;
}
*{margin:0;padding:0;box-sizing:border-box}
html,body{width:873px;height:1200px;overflow:hidden}
body{position:relative;background:var(--page);font-family:Arial,Helvetica,sans-serif;color:var(--text)}
.abs{position:absolute}
.nav{left:0;top:0;width:873px;height:69px;background:linear-gradient(#d4d4d4,#bdbdbd);border-bottom:1px solid #aaa}
.nav .sep{position:absolute;top:0;width:1px;height:69px;background:#e8e8e8}
.nav .item{position:absolute;top:45px;color:#fff;font-size:11px;font-weight:bold;transform:translateX(-50%)}
.nav .active{position:absolute;left:625px;top:0;width:73px;height:69px;background:linear-gradient(#b9d4e6,#8fb7d2)}
.banner{left:0;top:76px;width:873px;height:175px;background:radial-gradient(circle at 70% 40%,#9fd0f5,#2a78c4 50%,#0d3f86)}
.brand-name{left:194px;top:134px;font-family:"Rosario",sans-serif;font-size:33px;letter-spacing:6px;color:#fff}
.brand-tag{left:222px;top:170px;font-family:"Rosario",sans-serif;font-size:20px;letter-spacing:1px;color:var(--orange-light)}
.callout{right:83px;top:112px;text-align:right;color:#fff;font-family:"Noto Serif",serif;font-size:18px;line-height:22px}
.intro-title{left:136px;top:274px;font-family:"Rosario",sans-serif;font-size:21px;color:var(--orange)}
.intro{left:136px;top:311px;width:592px;font-size:10px;line-height:18px;color:#555}
.intro b{color:var(--orange)}
.tab{width:215px;height:46px;border-radius:6px;background:linear-gradient(#fde3a8,var(--orange-light) 45%,var(--orange));border:2px solid #fff;box-shadow:0 2px 3px rgba(0,0,0,.25)}
.tab span{position:absolute;left:78px;top:9px;font-family:"Rosario",sans-serif;font-size:21px;color:var(--navy)}
.tab .icon{position:absolute;left:12px;top:-12px;width:38px;height:46px;border-radius:6px;background:var(--blue)}
.list{list-style:none}
.list li{position:absolute;width:178px;height:22px;border-bottom:1px dotted var(--dots);font-size:10.5px;font-weight:bold;color:var(--blue);padding-left:18px;padding-top:4px}
.list li::before{content:"";position:absolute;left:2px;top:5px;border-left:8px solid var(--orange);border-top:4px solid transparent;border-bottom:4px solid transparent}
.list li.b::before{border-left-color:var(--blue)}
.divider{left:448px;top:397px;height:679px;border-left:1px dotted var(--dots)}
.card{background:#fff;box-shadow:0 3px 4px rgba(0,0,0,.2)}
.badge{background:var(--blue);color:#fff;font-size:7px;font-weight:bold;padding:2px 5px}
.card-title{font-size:16px;color:var(--blue)}
.card-link{font-size:9px;color:#444}
.post h3{font-size:10px;font-weight:bold;color:var(--blue);margin-bottom:1px}
.post p{font-size:10px;line-height:12px;color:#444;width:326px}
.post-line{height:1px;background:#e2e2e2;width:265px}
.ribbon{width:20px;height:27px}
.about{left:89px;top:957px;width:352px;font-size:8.6px;line-height:20.3px;color:#333}
.footer{left:0;top:1121px;width:873px;height:79px;background:#fafafa;border-top:1px solid #e2e2e2}
.chamber{left:88px;top:1148px;font-size:15px;font-weight:bold;color:var(--navy);line-height:14px}
.chamber small{display:block;font-size:7.5px;letter-spacing:.3px}
.flink{font-size:8.5px;font-weight:bold;color:#333;line-height:17px}
.fmeta{right:87px;top:1138px;text-align:right;font-size:8.5px;line-height:17.5px;color:#444}
.fmeta b{color:var(--orange)}
</style>
</head>
<body>

<nav class="abs nav">
  <div class="active"></div>
  <div class="sep" style="left:79px"></div><div class="sep" style="left:152px"></div>
  <div class="sep" style="left:249px"></div><div class="sep" style="left:355px"></div>
  <div class="sep" style="left:420px"></div><div class="sep" style="left:542px"></div>
  <div class="sep" style="left:625px"></div><div class="sep" style="left:698px"></div>
  <div class="sep" style="left:793px"></div>
  <svg class="abs" style="left:102px;top:28px" width="28" height="26" viewBox="0 0 28 26" aria-label="Home">
    <path d="M14 1 L1 13 L5 13 L5 25 L11 25 L11 17 L17 17 L17 25 L23 25 L23 13 L27 13 Z" fill="#fff"/>
  </svg>
  <span class="item" style="left:200px">SERVICES</span>
  <span class="item" style="left:300px">PORTFOLIO</span>
  <span class="item" style="left:386px">RFQ</span>
  <span class="item" style="left:480px">TESTIMONIALS</span>
  <span class="item" style="left:583px">ABOUT</span>
  <span class="item" style="left:660px">BLOG</span>
  <span class="item" style="left:745px">CONTACT</span>
</nav>

<header class="abs banner" role="img" aria-label="Blue bokeh light background"></header>
<div class="abs brand-name">FROSTLANE</div>
<div class="abs brand-tag">Website Design</div>
<div class="abs callout">Free<br>Consultation<br><span style="display:inline-block;margin-top:2px">555.204.7731</span><br>Call Now</div>

<h1 class="abs intro-title" style="font-weight:400">Websites that get results</h1>
<p class="abs intro"><b>70% of US households use the internet</b> when searching for local products and services. While most purchases are made offline (67%), they start online at the businesses website. If your website looks unprofessional or cannot be found <b>you are missing out on potential revenue</b> and a steady stream of new customers.</p>

<div class="abs tab" style="left:88px;top:404px"><div class="icon" role="img" aria-label="Paint brush icon"></div><span>What we do</span></div>
<div class="abs tab" style="left:466px;top:404px"><div class="icon" style="border-radius:50%;width:42px;height:42px;top:-4px" role="img" aria-label="Gear icon"></div><span>Our Blog</span></div>

<ul class="list">
  <li style="left:90px;top:467px">WEBSITE DESIGN</li>
  <li style="left:90px;top:494px">WEBSITE RE-DESIGN</li>
  <li class="b" style="left:90px;top:520px">ECOMMERCE</li>
  <li class="b" style="left:90px;top:546px">MOBILE WEBSITES</li>
  <li style="left:90px;top:572px">COPYWRITING</li>
  <li class="b" style="left:250px;top:469px">HOSTING AND MAINTENANCE</li>
  <li style="left:250px;top:495px">CONTENT MARKETING</li>
  <li class="b" style="left:250px;top:522px">PAY PER CLICK MARKETING</li>
  <li style="left:250px;top:548px">MOBILE TEXT MARKETING</li>
  <li style="left:250px;top:574px">LOCAL SEARCH MARKETING</li>

  <li style="left:468px;top:467px">LOCAL SEO</li>
  <li style="left:468px;top:494px">LOCAL BUSINESS MARKETING</li>
  <li class="b" style="left:468px;top:520px">LOCAL BUSINESS WEBSITES</li>
  <li class="b" style="left:468px;top:546px">CLIENT TESTIMONIALS</li>
  <li style="left:468px;top:572px">WEB DESIGN SERVICES</li>
  <li class="b" style="left:468px;top:598px">NEWSLETTERS</li>
  <li class="b" style="left:655px;top:469px;width:138px">COPYWRITING</li>
  <li style="left:655px;top:495px;width:138px">HELPFUL FINDINGS</li>
  <li class="b" style="left:655px;top:522px;width:138px">CLIENTS WEBSITES</li>
  <li style="left:655px;top:548px;width:138px">FEATURED CLIENTS</li>
  <li style="left:655px;top:574px;width:138px">SOCIAL MEDIA</li>
</ul>

<div class="abs divider"></div>

<div class="abs" style="left:90px;top:636px;width:152px;height:160px">
  <div class="badge" style="position:absolute;left:0;top:0;width:84px">ECOMMERCE</div>
  <div style="position:absolute;left:0;top:13px;width:152px;height:32px;background:#fff;font-size:17px;color:#333;text-align:center;line-height:32px">Cartwell</div>
  <div style="position:absolute;left:2px;top:45px;width:150px;height:115px;background:linear-gradient(135deg,#0f7fa8,#0b5f86)" role="img" aria-label="Online store page mockups"></div>
</div>
<div class="abs card-title" style="left:99px;top:804px">Ecommerce</div>
<div class="abs card-link" style="left:99px;top:825px;text-decoration:underline">Details</div>

<div class="abs card" style="left:269px;top:650px;width:153px;height:208px">
  <div style="position:absolute;left:0;top:0;width:153px;height:148px;background:linear-gradient(135deg,#6fc6ee,#2b9fde)" role="img" aria-label="Search engine cards on a code background"></div>
  <div class="card-title" style="position:absolute;left:10px;top:156px">Search Marketing</div>
  <div class="card-link" style="position:absolute;left:10px;top:177px">Details...</div>
</div>
<div class="abs badge" style="left:269px;top:638px">SEARCH MARKETING</div>

<div class="abs tab" style="left:466px;top:650px"><div class="icon" style="transform:rotate(40deg);width:14px;height:56px;left:28px;top:-10px" role="img" aria-label="Pencil icon"></div><span>Blog Postings</span></div>

<div class="abs post" style="left:461px;top:727px">
  <h3>Making Your Website Work For You</h3>
  <p>Praesent ac enim sed velit ornare condimentum. Nulla blandit porta arcu vestibulum sollicitudin. Ut accumsan id eros eu lacinia. Nullam blandit turpis sem. Phasellus consequat ante a ultrices dapibus. Fusce vitae mauris tempus, elementum quam sit amet, scelerisque orci.</p>
</div>
<div class="abs post" style="left:461px;top:838px">
  <h3>Making Your Website Work For You</h3>
  <p>Praesent ac enim sed velit ornare condimentum. Nulla blandit porta arcu vestibulum sollicitudin. Ut accumsan id eros eu lacinia. Nullam blandit turpis sem. Phasellus consequat ante a ultrices dapibus. Fusce vitae mauris tempus, elementum quam sit amet, scelerisque orci.</p>
</div>
<div class="abs post" style="left:461px;top:952px">
  <h3>Making Your Website Work For You</h3>
  <p>Praesent ac enim sed velit ornare condimentum. Nulla blandit porta arcu vestibulum sollicitudin. Ut accumsan id eros eu lacinia. Nullam blandit turpis sem. Phasellus consequat ante a ultrices dapibus. Fusce vitae mauris tempus, elementum quam sit amet, scelerisque orci.</p>
</div>

<div class="abs post-line" style="left:528px;top:797px"></div>
<div class="abs post-line" style="left:528px;top:909px"></div>
<div class="abs post-line" style="left:528px;top:1023px"></div>
<svg class="abs ribbon" style="left:769px;top:799px" viewBox="0 0 20 27" aria-label="More"><path d="M0 0H20V27L10 20L0 27Z" fill="var(--blue)"/><path d="M10 4V12M6 8H14" stroke="#fff" stroke-width="1.6"/></svg>
<svg class="abs ribbon" style="left:769px;top:911px" viewBox="0 0 20 27" aria-label="More"><path d="M0 0H20V27L10 20L0 27Z" fill="var(--blue)"/><path d="M10 4V12M6 8H14" stroke="#fff" stroke-width="1.6"/></svg>
<svg class="abs ribbon" style="left:769px;top:1025px" viewBox="0 0 20 27" aria-label="More"><path d="M0 0H20V27L10 20L0 27Z" fill="var(--blue)"/><path d="M10 4V12M6 8H14" stroke="#fff" stroke-width="1.6"/></svg>

<div class="abs tab" style="left:88px;top:891px"><div class="icon" style="width:34px;height:52px;top:-14px;left:24px;border-radius:4px 4px 10px 10px" role="img" aria-label="Paint bucket icon"></div><span>Web Design</span></div>

<p class="abs about">FrostLane, a leading professional web design and web development company operating out of Harrow county in northeastern Pennsylvania, serves businesses everywhere...from down the street to across the country. No matter what your web needs might be, or the industry you service, we can help you achieve results by specializing in... Web Design &nbsp;/&nbsp; e-Commerce &nbsp;/&nbsp; Text Message Marketing &nbsp;/&nbsp; Search Engine Optimization &nbsp;/&nbsp; Mobile Websites</p>

<footer class="abs footer"></footer>
<div class="abs chamber">HARROW VALLEY<small>CHAMBER OF COMMERCE</small></div>
<div class="abs flink" style="left:297px;top:1143px">Home<br>Services</div>
<div class="abs flink" style="left:376px;top:1141px">Portfolio<br>Contact Us</div>
<div class="abs flink" style="left:472px;top:1141px">Request a Quote<br>Associates</div>
<div class="abs fmeta">© 2008 - 2012 FrostLane Website Design<br>Twelve Mill Lane - Brookhaven, PA 18230<br>(800) 555-0142 - (555) 204-7731 - <b>Live Support</b></div>

</body>
</html>
```